Hvac and insulation company needs good looking business card design

We are hvac and insulation company and looking for a new business cards that look to today standards designs

Target Market(s)

homeowners

Industry/Entity Type

Hvac

Contact Information for Business Card

Name: Dorian Velkova
Home comfort consultant
address: 4827 Marrow Ridge Rd #215 Brookvale, CA 94582
office: 888-317-5069
cell: 510-642-1388
Lic.# 458127
Email: dorian@quarry-hvac.com
Web: quarry-hvac.com

Requirements
Must have
• clean and sleek look
Nice to have
• simple with a clean look
Should not have
• to busy business card

```html
<!DOCTYPE html>
<html lang="en">
<head>
<meta charset="utf-8">
<title>Quarry Home Solutions – Business Card</title>
<link rel="stylesheet" href="https://fonts.googleapis.com/css2?family=Arimo:wght@400;700&family=Open+Sans:wght@400;600&display=swap">
<style>
  :root {
    --brand-orange: #ee8322;
    --ink-grey: #555555;
    --swoosh-grey: #8a8a8a;
    --card-white: #fafafa;
    --backdrop: #e4e4e4;
  }
  * { box-sizing: border-box; margin: 0; padding: 0; }
  html, body { width: 1200px; height: 786px; overflow: hidden; }
  body {
    background: var(--backdrop);
    display: flex;
    align-items: center;
    justify-content: center;
    gap: 40px;
    font-family: "Arimo", Arial, sans-serif;
  }
  .card {
    position: relative;
    width: 520px;
    height: 297px;
    border-radius: 14px;
    overflow: hidden;
    box-shadow: 0 6px 18px rgba(0,0,0,0.18);
  }

  /* Front */
  .card-front {
    background: var(--brand-orange);
    display: flex;
    align-items: center;
    justify-content: center;
  }
  .wordmark { display: flex; align-items: center; gap: 12px; }
  .wordmark-square {
    width: 30px; height: 30px;
    background: currentColor;
    border-radius: 3px;
  }
  .wordmark-text { display: flex; flex-direction: column; }
  .wordmark-name {
    font-family: "Open Sans", Arial, sans-serif;
    font-weight: 600;
    line-height: 1;
  }
  .wordmark-tagline {
    font-family: "Open Sans", Arial, sans-serif;
    font-weight: 400;
    letter-spacing: 0.22em;
  }
  .card-front .wordmark { color: #ffffff; }
  .card-front .wordmark-name { font-size: 56px; }
  .card-front .wordmark-tagline { font-size: 15px; margin-top: 2px; }

  /* Back */
  .card-back { background: var(--card-white); }
  .holder { position: absolute; left: 34px; top: 34px; }
  .holder-name {
    color: var(--brand-orange);
    font-weight: 700;
    font-size: 17px;
    text-transform: uppercase;
    letter-spacing: 0.01em;
  }
  .holder-title { color: var(--ink-grey); font-size: 12px; margin-top: 4px; }

  .contact-list {
    position: absolute; left: 34px; top: 112px;
    list-style: none;
    color: var(--ink-grey);
    font-size: 12px;
    line-height: 18px;
  }
  .contact-list li { display: flex; align-items: center; gap: 7px; }
  .contact-icon { width: 10px; height: 10px; flex: none; }

  .card-back .wordmark {
    position: absolute; right: 44px; top: 118px;
    color: var(--brand-orange);
  }
  .card-back .wordmark-name { font-size: 40px; }
  .card-back .wordmark-square { width: 22px; height: 22px; }
  .card-back .wordmark-tagline { font-size: 11px; color: var(--ink-grey); }

  .address {
    position: absolute; right: 44px; bottom: 30px;
    text-align: right;
    color: var(--ink-grey);
    font-size: 12px;
    line-height: 16px;
    font-style: normal;
  }
  .swoosh { position: absolute; left: 0; bottom: 0; width: 520px; height: 297px; }
</style>
</head>
<body>

  <section class="card card-front" aria-label="Card front">
    <div class="wordmark">
      <span class="wordmark-square"></span>
      <div class="wordmark-text">
        <span class="wordmark-name">quarry</span>
        <span class="wordmark-tagline">home solutions</span>
      </div>
    </div>
  </section>

  <section class="card card-back" aria-label="Card back">
    <svg class="swoosh" viewBox="0 0 520 297" aria-hidden="true">
      <path d="M0 150 C 40 240, 150 280, 250 297 L0 297 Z" fill="var(--swoosh-grey)"/>
      <path d="M0 150 C 40 240, 150 280, 250 297 L235 297 C 140 282, 35 245, 0 170 Z" fill="#ffffff"/>
      <path d="M0 132 C 45 235, 160 278, 270 297 L258 297 C 150 280, 40 240, 0 146 Z" fill="var(--brand-orange)"/>
    </svg>

    <div class="holder">
      <p class="holder-name">Dorian Velkova</p>
      <p class="holder-title">Home comfort consultant</p>
    </div>

    <ul class="contact-list">
      <li>
        <svg class="contact-icon" viewBox="0 0 10 10"><rect x="2" y="0.5" width="6" height="9" rx="1" fill="none" stroke="var(--brand-orange)" stroke-width="1.3"/></svg>
        510-642-1388
      </li>
      <li>
        <svg class="contact-icon" viewBox="0 0 10 10"><path d="M2 0.5 L4 3 L3 4.5 C4 6.5 5 7 6 7.5 L7.5 6.5 L9.5 8.5 L8 9.8 C4 9 1 6 0.3 2 Z" fill="var(--brand-orange)"/></svg>
        888-317-5069
      </li>
      <li>
        <svg class="contact-icon" viewBox="0 0 10 10"><rect x="0.5" y="2" width="9" height="6.5" fill="var(--brand-orange)"/><path d="M0.5 2 L5 5.5 L9.5 2" fill="none" stroke="#fff" stroke-width="1"/></svg>
        dorian@quarry-hvac.com
      </li>
      <li>
        <svg class="contact-icon" viewBox="0 0 10 10"><circle cx="5" cy="5" r="4.5" fill="var(--brand-orange)"/><path d="M0.5 5 H9.5 M5 0.5 C2.5 3 2.5 7 5 9.5 M5 0.5 C7.5 3 7.5 7 5 9.5" fill="none" stroke="#fff" stroke-width="0.8"/></svg>
        www.quarry-hvac.com
      </li>
    </ul>

    <div class="wordmark">
      <span class="wordmark-square"></span>
      <div class="wordmark-text">
        <span class="wordmark-name">quarry</span>
        <span class="wordmark-tagline">home solutions</span>
      </div>
    </div>

    <address class="address">
      4827 Marrow Ridge Rd #215<br>
      Brookvale, CA 94582<br>
      Lic.# 458127
    </address>
  </section>

</body>
</html>
```